Tech Savy small Business accountant business card design

We need a business card for a new company based in the cloud. We provide tax, business advisory, accounting, information technology solutions and back office functions to small businesses. We offer fixed fee packages with add on services as you need them. By harnessing technology we simplify small business operational processes providing valuable time and information for small business owners to grow their business. In the logo (quilbrook) we want to be able to see quil and experts. The final design should communicate achieving growth dreams and balance (ie life and $).
Updates
This project has been temporarily placed on hold until I finalize "Tech Savy small Business accountant needs a logo". I invite all designers to submit on this logo project. Once my logo is finalized I will resume this business card contest. Thanks Added Wednesday, March 19, 2014
This project has been temporarily placed on hold until I finalize "Tech Savy small Business accountant logo". I invite all designers to submit on this logo project. Once my logo is finalized I will resume this business card contest. Thanks Added Thursday, March 20, 2014
Target Market(s)
Small Business (Revenue $500,000, more than 3 employees) owners.
Industry/Entity Type
Small Business
Contact Information for Business Card
Marla Henwick (Principal)
Accountant, Tax Agent.
TEL | 0418 663 904
EMAIL | Marla.Henwick@quilbrook-mail.com.au
WEB | www.quilbrook-mail.com.au
Look and feel

```html
<!DOCTYPE html>
<html lang="en">
<head>
<meta charset="utf-8">
<title>quilbrook business card</title>
<link rel="stylesheet" href="https://fonts.googleapis.com/css2?family=Open+Sans:wght@400;700;800&display=swap">
<style>
  :root {
    --bg: #e9e6e1;
    --blue-light: #5ec2ef;
    --blue: #2b9fe0;
    --blue-deep: #1068b8;
    --black: #0b0b0d;
    --grey: #6b6d72;
    --grey-dark: #3c3d41;
    --white: #ffffff;
  }
  html, body {
    margin: 0;
    width: 1200px;
    height: 913px;
    overflow: hidden;
    background: var(--bg);
    font-family: "Open Sans", Arial, sans-serif;
  }
  .sheet {
    position: relative;
    width: 1200px;
    height: 913px;
  }
  .card {
    position: absolute;
    width: 520px;
    height: 318px;
    overflow: hidden;
    box-shadow: 0 10px 26px rgba(0,0,0,.25);
  }
  .card-front { left: 50px; top: 160px; background: var(--black); }
  .card-back {
    left: 630px; top: 435px;
    background: linear-gradient(160deg, var(--blue-light) 0%, var(--blue) 45%, var(--blue-deep) 100%);
  }
  .card-art { position: absolute; inset: 0; }
  .holder {
    position: absolute;
    left: 34px; top: 128px;
    color: var(--white);
  }
  .holder-name {
    margin: 0;
    font-size: 17px;
    font-weight: 700;
    letter-spacing: .2px;
  }
  .holder-name .role { text-transform: none; }
  .holder-title {
    margin: 2px 0 0;
    font-size: 12.5px;
    font-weight: 400;
  }
  .brand { position: absolute; color: var(--white); }
  .brand-name {
    margin: 0;
    font-weight: 800;
    line-height: 1;
    letter-spacing: -1px;
  }
  .brand-tag { margin: 0; font-weight: 400; }
  .card-front .brand { left: 318px; top: 96px; }
  .card-front .brand-name { font-size: 38px; }
  .card-front .brand-tag { font-size: 10.5px; margin-top: 3px; }
  .card-back .brand {
    left: 0; right: 0; top: 104px;
    text-align: center;
  }
  .card-back .brand-name { font-size: 76px; letter-spacing: -2px; }
  .card-back .brand-tag { font-size: 17px; margin-top: 4px; }
  .contacts {
    position: absolute;
    left: 156px; top: 236px;
    margin: 0; padding: 0;
    list-style: none;
    color: var(--white);
    font-size: 12.5px;
    line-height: 19px;
  }
  .contacts li { display: flex; align-items: center; gap: 8px; }
  .contacts svg { width: 11px; height: 11px; flex: none; }
</style>
</head>
<body>
<main class="sheet">

  <section class="card card-front" aria-label="Business card front">
    <svg class="card-art" viewBox="0 0 520 318" aria-hidden="true">
      <defs>
        <linearGradient id="front-blue" x1="0" y1="0" x2="1" y2="1">
          <stop offset="0" stop-color="#4fb8ee"/>
          <stop offset="1" stop-color="#1f8ad6"/>
        </linearGradient>
        <linearGradient id="front-grey" x1="0" y1="0" x2="1" y2="0">
          <stop offset="0" stop-color="#7a7c81"/>
          <stop offset="1" stop-color="#2e2f33"/>
        </linearGradient>
      </defs>
      <polygon fill="url(#front-blue)" points="0,0 305,0 392,150 520,168 150,176 96,202 0,214"/>
      <polygon fill="url(#front-grey)" points="0,214 96,202 150,176 520,168 160,196 118,232 0,244"/>
    </svg>

    <div class="holder">
      <h1 class="holder-name">MARLA HENWICK <span class="role">(Principal)</span></h1>
      <p class="holder-title">Accountant, Tax Agent</p>
    </div>

    <div class="brand">
      <p class="brand-name">quilbrook</p>
      <p class="brand-tag">Your business and accounting partner</p>
    </div>

    <ul class="contacts">
      <li>
        <svg viewBox="0 0 12 12"><path fill="#2b9fe0" d="M2.5 1l2 2-1 1.3a7 7 0 0 0 4.2 4.2L9 7.5l2 2-1.5 1.5C5 11 1 7 1 2.5z"/></svg>
        0418 663 904
      </li>
      <li>
        <svg viewBox="0 0 12 12"><g fill="none" stroke="#2b9fe0" stroke-width="1.2"><circle cx="6" cy="6" r="5"/><ellipse cx="6" cy="6" rx="2.2" ry="5"/><path d="M1 6h10"/></g></svg>
        www.quilbrook-mail.com.au
      </li>
      <li>
        <svg viewBox="0 0 12 12"><g fill="none" stroke="#2b9fe0" stroke-width="1.2"><rect x="1" y="2.5" width="10" height="7"/><path d="M1 2.5l5 4 5-4"/></g></svg>
        Marla.Henwick@quilbrook-mail.com.au
      </li>
    </ul>
  </section>

  <section class="card card-back" aria-label="Business card back">
    <div class="brand">
      <p class="brand-name">quilbrook</p>
      <p class="brand-tag">Your business and accounting partner</p>
    </div>
  </section>

</main>
</body>
</html>
```